Poster for The Hearthstone Pantry

Simple, light, "earthy" looking poster advertising Australia's newest online paleo store. Making your paleo lifestyle easy.

The Hearthstone Pantry is an Australian owned & operated online store with a team dedicated to sourcing only the best paleo-friendly products in the marketplace and delivering you a convenient one-stop location from which to buy them. We offer a wide range of foods for all occasions including breakfast options, lunches, snacks & desserts plus all your cooking basics to prepare delicious paleo dinners.

We also offer a range of books essential to all paleo kitchens containing hundreds of mouthwatering recipes. Visit our blog which is regularly updated with our favourite paleo dishes, tips & tricks.

Target Market(s)

Health-conscious, IronLoopers, Overweight people

Industry/Entity Type

Advertising

Requirements
Must have
• The Hearthstone Pantry logo (uploaded) and colouring from background from website (uploaded) - we want to keep a consistent image. Light colours over dark colours preferred.

Must have notes to "Like The Hearthstone Pantry on Friendbook" and "Follow us on Chirper @thehearthstonepantry"

Nice to have
• Could include parts of below text - I like the idea of bolding and increasing the font size of certain key words such as "Australian owned & operated" and "best paleo-friendly products" etc...so they stand out from the paragraph -

"The Hearthstone Pantry is an Australian owned & operated online store with a team dedicated to sourcing only the best paleo-friendly products in the marketplace and delivering you a convenient one-stop location from which to buy them. We offer a wide range of foods for all occasions including breakfast options, lunches, snacks & desserts plus all your cooking basics to prepare delicious paleo dinners.

We also offer a range of books essential to all paleo kitchens containing hundreds of mouthwatering recipes. Visit our blog which is regularly updated with our favourite paleo dishes, tips & tricks."

```html
<!DOCTYPE html>
<html lang="en">
<head>
<meta charset="utf-8">
<title>The Hearthstone Pantry – Poster</title>
<link rel="stylesheet" href="https://fonts.googleapis.com/css2?family=Questrial&family=Ubuntu:wght@400;500;700&display=swap">
<style>
  :root {
    --ink: #3d3935;
    --ink-strong: #2a2622;
    --brand-green: #7ea33a;
    --olive: #6d7b1e;
    --cream: #fffaf0;
    --peach: #f6c99a;
    --sun: #fff6d8;
    --hill-light: #c9c25a;
    --hill-mid: #8fa63c;
    --hill-dark: #4f7a2c;
    --white: #ffffff;
  }
  html, body {
    margin: 0;
    padding: 0;
    overflow: hidden;
    background: var(--cream);
  }
  .poster {
    position: relative;
    width: 927px;
    height: 1200px;
    overflow: hidden;
    font-family: "Questrial", "Helvetica Neue", Arial, sans-serif;
    color: var(--ink);
    background:
      radial-gradient(ellipse 70% 55% at 50% 62%, var(--sun) 0%, #fde7c4 35%, var(--peach) 70%, #f9dcc0 100%);
  }
  .sunburst {
    position: absolute;
    inset: 0;
    background: radial-gradient(circle at 50% 62%, rgba(255,255,255,0.85) 0%, rgba(255,255,255,0) 45%);
  }
  .hills {
    position: absolute;
    left: -120px;
    right: -120px;
    top: 800px;
    bottom: 0;
    border-radius: 60% 40% 0 0 / 28% 22% 0 0;
    background: linear-gradient(160deg, var(--hill-light) 0%, var(--hill-mid) 40%, var(--hill-dark) 75%, var(--hill-mid) 100%);
  }
  .headline {
    position: absolute;
    top: 50px;
    left: 0;
    width: 100%;
    margin: 0;
    text-align: center;
    font-weight: 400;
    font-size: 33px;
    line-height: 44px;
    letter-spacing: 0.5px;
    text-transform: uppercase;
    color: var(--ink);
  }
  .brand-name {
    position: absolute;
    top: 205px;
    left: 0;
    width: 100%;
    margin: 0;
    text-align: center;
    font-weight: 400;
    font-size: 96px;
    line-height: 104px;
    color: var(--brand-green);
  }
  .intro {
    position: absolute;
    top: 490px;
    right: 66px;
    width: 820px;
    margin: 0;
    text-align: right;
    font-size: 21.5px;
    line-height: 32.5px;
    color: var(--ink);
  }
  .intro strong {
    font-weight: 400;
    font-size: 23px;
    color: var(--ink-strong);
    text-shadow: 0.5px 0 0 var(--ink-strong);
  }
  .tagline {
    position: absolute;
    top: 728px;
    left: 0;
    width: 100%;
    margin: 0;
    text-align: center;
    font-size: 39px;
    color: var(--olive);
  }
  .cta {
    position: absolute;
    top: 812px;
    left: 0;
    width: 100%;
    margin: 0;
    text-align: center;
    font-family: "Ubuntu", Arial, sans-serif;
    font-weight: 500;
    font-size: 36px;
    color: #4a4036;
  }
  .rule {
    position: absolute;
    left: 150px;
    width: 600px;
    height: 3px;
    background: #4a4036;
    border-radius: 2px;
  }
  .rule--top { top: 872px; }
  .rule--bottom { top: 936px; }
  .web-address {
    position: absolute;
    top: 880px;
    left: 0;
    width: 100%;
    margin: 0;
    text-align: center;
    font-family: "Ubuntu", Arial, sans-serif;
    font-size: 44px;
    color: var(--white);
    text-shadow: -1.5px -1.5px 0 #3b3430, 1.5px -1.5px 0 #3b3430, -1.5px 1.5px 0 #3b3430, 1.5px 1.5px 0 #3b3430;
  }
  .social {
    position: absolute;
    left: 56px;
    top: 1036px;
    margin: 0;
    padding: 0;
    list-style: none;
    font-size: 21px;
    color: var(--white);
  }
  .social li {
    display: flex;
    align-items: center;
    height: 30px;
    margin-bottom: 14px;
    text-shadow: 0 0 2px rgba(40,50,20,0.6);
  }
  .social .name {
    font-size: 23px;
    color: #3b3430;
    text-shadow: none;
  }
  .social-square {
    width: 24px;
    height: 24px;
    margin-right: 10px;
    border-radius: 3px;
    background: #5b79b0;
  }
  .social-square--chirper { background: #6fb4d6; }
  .contact {
    position: absolute;
    left: 58px;
    top: 1136px;
    margin: 0;
    font-size: 23px;
    color: var(--ink-strong);
  }
  .contact em {
    color: var(--white);
    margin-left: 4px;
  }
</style>
</head>
<body>
<main class="poster">
  <div class="sunburst" role="img" aria-label="Soft sun rays radiating from behind the hills"></div>
  <div class="hills" role="img" aria-label="Rolling green and golden hills"></div>

  <h2 class="headline">Australian owned &amp; operated online store<br>open for business</h2>

  <h1 class="brand-name">The Hearthstone<br>Pantry</h1>

  <p class="intro">
    with a team dedicated to sourcing only the<br>
    <strong>best paleo-friendly products</strong> in the marketplace and delivering<br>
    you a <strong>convenient one-stop location</strong> from which to buy them.<br>
    We offer a wide range of foods for all occasions including <strong>breakfast</strong><br>
    options, <strong>lunches, snacks &amp; desserts</strong> plus all your <strong>cooking basics</strong><br>
    <strong>&amp; recipe books</strong> to prepare delicious paleo dinners.
  </p>

  <p class="tagline">“Eat the way nature intended”</p>

  <p class="cta">shop online today</p>
  <div class="rule rule--top"></div>
  <p class="web-address">www.thehearthstonepantry.com.au</p>
  <div class="rule rule--bottom"></div>

  <ul class="social">
    <li><span class="social-square"></span>Like&nbsp;<span class="name">THE HEARTHSTONE PANTRY</span>&nbsp;on Friendbook</li>
    <li><span class="social-square social-square--chirper"></span>Follow Us on Chirper&nbsp;<span class="name">@thehearthstonepantry</span></li>
  </ul>

  <p class="contact">Contact us <em>info@thehearthstonepantry.com.au</em></p>
</main>
</body>
</html>
```